Australian IT Company requires Business Card Design

Bluewattle is an Australian company that specialises in IT consulting & support, software development, project management, network services.

We have been in business for 15 years.

* We require a business card with the following on it:
Logo
Address
Contact Details
Space for staff name, title & mobile number

Industry/Entity Type

Software

```html
<!DOCTYPE html>
<html lang="en">
<head>
<meta charset="utf-8">
<title>Bluewattle Business Cards</title>
<link href="https://fonts.googleapis.com/css2?family=Open+Sans:wght@400;600;700&display=swap" rel="stylesheet">
<style>
  :root {
    --blue: #3f7fb3;
    --blue-light: #6aa6d2;
    --grey: #6f7173;
    --ink: #4a4b4d;
    --muted: #9a9b9d;
    --paper: #ffffff;
    --backdrop: #e9e7e3;
  }
  * { margin: 0; padding: 0; box-sizing: border-box; }
  html, body { width: 1200px; height: 1000px; overflow: hidden; }
  body {
    background: var(--backdrop);
    font-family: "Open Sans", Arial, sans-serif;
    position: relative;
  }
  .card {
    position: absolute;
    left: 250px;
    width: 700px;
    height: 400px;
    background: var(--paper);
    overflow: hidden;
    box-shadow: 0 6px 18px rgba(0,0,0,0.18);
  }
  .card--primary { top: 70px; }
  .card--alternate { top: 530px; }
  .card__shapes { position: absolute; inset: 0; }
  .brand {
    position: absolute;
    left: 40px;
    top: 44px;
    display: flex;
    align-items: center;
    gap: 12px;
  }
  .brand__square { width: 30px; height: 30px; background: var(--blue); flex: none; }
  .brand__name {
    font-size: 28px;
    font-weight: 700;
    color: var(--blue);
    line-height: 1;
  }
  .staff {
    position: absolute;
    text-align: center;
  }
  .card--primary .staff { left: 260px; top: 140px; }
  .card--alternate .staff { left: 300px; top: 150px; }
  .staff__name { font-size: 32px; font-weight: 700; color: var(--ink); line-height: 1.1; }
  .staff__position { font-size: 21px; color: var(--muted); }
  .contact {
    position: absolute;
    list-style: none;
    color: #fff;
    font-size: 17px;
    line-height: 1.55;
  }
  .contact li { display: flex; align-items: center; gap: 8px; }
  .contact svg { width: 15px; height: 15px; flex: none; }
  .card--primary .contact { left: 345px; top: 280px; }
  .card--alternate .contact { left: 195px; top: 282px; }
  .address {
    position: absolute;
    color: #fff;
    font-size: 17px;
    line-height: 1.4;
    font-style: normal;
  }
  .card--primary .address { left: 28px; top: 305px; }
  .card--alternate .address { left: 14px; top: 290px; font-size: 15px; }
</style>
</head>
<body>

<section class="card card--primary">
  <svg class="card__shapes" viewBox="0 0 700 400" aria-hidden="true">
    <polygon points="510,0 700,0 700,58 555,58" fill="var(--blue-light)"/>
    <polygon points="420,0 510,0 555,58 700,58 700,115 495,115" fill="var(--grey)"/>
    <polygon points="330,250 700,250 700,400 290,400" fill="var(--grey)"/>
    <polygon points="0,290 335,290 305,400 0,400" fill="var(--blue)"/>
  </svg>
  <div class="brand">
    <span class="brand__square"></span>
    <span class="brand__name">Bluewattle</span>
  </div>
  <div class="staff">
    <p class="staff__name">Staff Name</p>
    <p class="staff__position">staff position</p>
  </div>
  <ul class="contact">
    <li><svg viewBox="0 0 16 16"><path d="M4 1l3 3-2 2c1 2 3 4 5 5l2-2 3 3-2 3C7 15 1 9 1 3z" fill="#fff"/></svg>+61 3 9555 0142</li>
    <li><svg viewBox="0 0 16 16"><rect x="1" y="3" width="14" height="10" fill="#fff"/><path d="M1 3l7 6 7-6" stroke="var(--grey)" fill="none"/></svg>staffname@bluewattle.net.au</li>
    <li><svg viewBox="0 0 16 16"><circle cx="8" cy="8" r="7" fill="#fff"/><path d="M1 8h14M8 1v14M3 4h10M3 12h10" stroke="var(--grey)" stroke-width="0.9"/></svg>www.bluewattle.net.au</li>
  </ul>
  <address class="address">14 Harbour Lane<br>Tech Hub 3<br>Greenvale Vic 3059</address>
</section>

<section class="card card--alternate">
  <svg class="card__shapes" viewBox="0 0 700 400" aria-hidden="true">
    <polygon points="560,0 630,0 700,70 700,190" fill="var(--grey)"/>
    <polygon points="630,0 700,0 700,70" fill="var(--blue)"/>
    <polygon points="170,255 480,255 540,400 170,400" fill="var(--grey)"/>
    <polygon points="0,265 170,265 170,400 0,400" fill="var(--blue)"/>
  </svg>
  <div class="brand">
    <span class="brand__square"></span>
    <span class="brand__name">Bluewattle</span>
  </div>
  <div class="staff">
    <p class="staff__name">Staff Name</p>
    <p class="staff__position">staff position</p>
  </div>
  <ul class="contact">
    <li><svg viewBox="0 0 16 16"><path d="M4 1l3 3-2 2c1 2 3 4 5 5l2-2 3 3-2 3C7 15 1 9 1 3z" fill="#fff"/></svg>+61 3 9555 0142</li>
    <li><svg viewBox="0 0 16 16"><rect x="1" y="3" width="14" height="10" fill="#fff"/><path d="M1 3l7 6 7-6" stroke="var(--grey)" fill="none"/></svg>staffname@bluewattle.net.au</li>
    <li><svg viewBox="0 0 16 16"><circle cx="8" cy="8" r="7" fill="#fff"/><path d="M1 8h14M8 1v14M3 4h10M3 12h10" stroke="var(--grey)" stroke-width="0.9"/></svg>www.bluewattle.net.au</li>
  </ul>
  <address class="address">14 Harbour Lane<br>Tech Hub 3<br>Greenvale Vic 3059</address>
</section>

</body>
</html>
```